Creating a Label for the Wine "Viña Aldaluz"

Viña Aldaluz
Viña Aldaluz means “lost mountain. Viña Aldaluz is a mountain far away from everything, lost in a wild place. The dimensios shoul be between 9cm x 11,5 cm and 12cm x 8 cm.

```html
<!DOCTYPE html>
<html lang="es">
<head>
<meta charset="utf-8">
<title>Viña Aldaluz – Wine Label</title>
<link rel="stylesheet" href="https://fonts.googleapis.com/css2?family=Cinzel:wght@400;500&family=Pinyon+Script&display=swap">
<style>
  :root {
    --page-bg: #ffffff;
    --label-black: #0b0b0b;
    --label-charcoal: #1c1c1c;
    --gold-light: #e7c25a;
    --gold: #c99a2e;
    --gold-deep: #9a7020;
    --frame-gold: rgba(201, 154, 46, 0.55);
  }

  * { margin: 0; padding: 0; box-sizing: border-box; }

  html, body {
    width: 1200px;
    height: 1010px;
    overflow: hidden;
    background: var(--page-bg);
  }

  .canvas {
    position: relative;
    width: 1200px;
    height: 1010px;
  }

  .wine-label {
    position: absolute;
    left: 214px;
    top: 25px;
    width: 772px;
    height: 960px;
    background:
      radial-gradient(ellipse at 50% 40%, var(--label-charcoal) 0%, var(--label-black) 75%);
    color: var(--gold);
    text-align: center;
  }

  .label-frame {
    position: absolute;
    inset: 17px;
    border: 2px solid var(--frame-gold);
  }

  .gold-text {
    background: linear-gradient(180deg, var(--gold-light) 0%, var(--gold) 55%, var(--gold-deep) 100%);
    -webkit-background-clip: text;
    background-clip: text;
    color: transparent;
  }

  .peak-emblem {
    position: absolute;
    left: 270px;
    top: 114px;
    width: 284px;
    height: 198px;
  }

  .estate-name {
    position: absolute;
    left: 0;
    right: 0;
    top: 352px;
    font-family: "Cinzel", serif;
    font-weight: 400;
    font-size: 50px;
    letter-spacing: 1px;
    line-height: 1;
  }

  .estate-subtitle {
    position: absolute;
    left: 0;
    right: 0;
    top: 428px;
    font-family: "Cinzel", serif;
    font-weight: 400;
    font-size: 30px;
    letter-spacing: 3px;
    line-height: 1;
  }

  .wine-name {
    position: absolute;
    left: 0;
    right: 0;
    top: 560px;
    font-family: "Pinyon Script", cursive;
    font-size: 84px;
    line-height: 1;
  }

  .wine-region {
    position: absolute;
    left: 0;
    right: 0;
    top: 665px;
    font-family: "Cinzel", serif;
    font-weight: 500;
    font-size: 30px;
    letter-spacing: 3px;
    line-height: 1;
  }

  .vintage-line {
    position: absolute;
    left: 0;
    right: 0;
    top: 832px;
    font-family: "Cinzel", serif;
    font-weight: 400;
    font-size: 28px;
    letter-spacing: 2px;
    line-height: 1;
  }
</style>
</head>
<body>
  <main class="canvas">
    <section class="wine-label">
      <div class="label-frame"></div>

      <svg class="peak-emblem" viewBox="0 0 284 198" role="img" aria-label="Gold mountain peak emblem">
        <defs>
          <linearGradient id="emblemGold" x1="0" y1="0" x2="0" y2="1">
            <stop offset="0" stop-color="#e7c25a" stop-opacity="0.85"/>
            <stop offset="1" stop-color="#9a7020" stop-opacity="0.35"/>
          </linearGradient>
        </defs>
        <rect x="0" y="0" width="284" height="198" fill="url(#emblemGold)"/>
      </svg>

      <h1 class="estate-name gold-text">VINEYARD NAME</h1>
      <p class="estate-subtitle gold-text">VINEYARDS</p>

      <h2 class="wine-name gold-text">Viña Aldaluz</h2>
      <p class="wine-region gold-text">ARAGON SPAIN</p>

      <p class="vintage-line gold-text">2010 | ESTATE GROWN</p>
    </section>
  </main>
</body>
</html>
```